Design a business card for Brenton's Heat Guardian
Brenton's Heat Guardian
Design a business card for Brenton's Heat Guardian - Food
Creative Brief
Traditional
Hal Brenton
President and CEO
52894 Corvane Lane Clinton Township, MI 48052
hbrenton1947@mailvex.example
www.brentonsheatguardian.example
Simple color marks, with some white space to write notes

```html
<!DOCTYPE html>
<html lang="en">
<head>
<meta charset="utf-8">
<title>Brenton's Heat Guardian — Business Card</title>
<link href="https://fonts.googleapis.com/css2?family=Open+Sans:wght@400;600;700&display=swap" rel="stylesheet">
<style>
  :root {
    --backdrop: #e4e5e7;
    --card: #ffffff;
    --ink: #1a1a1a;
    --night: #151515;
    --flame: #f26a1b;
    --ember: #e23a1c;
    --gold: #f7c21b;
    --paper-text: #ffffff;
  }
  * { box-sizing: border-box; margin: 0; padding: 0; }
  html, body {
    width: 1200px; height: 908px; overflow: hidden;
    background: var(--backdrop);
    font-family: "Open Sans", Arial, sans-serif;
  }
  .stage { position: relative; width: 1200px; height: 908px; }

  .card {
    position: absolute;
    width: 540px; height: 310px;
    background: var(--card);
    border-radius: 16px;
    overflow: hidden;
    box-shadow: 0 6px 18px rgba(0,0,0,0.12);
  }
  .card--front { left: 50px; top: 190px; }
  .card--back  { left: 610px; top: 410px; }

  .brand { display: flex; align-items: center; gap: 10px; }
  .brand__dot {
    width: 14px; height: 14px; border-radius: 50%;
    background: var(--flame); flex: none;
  }
  .brand__name {
    font-weight: 700; color: var(--ink);
    font-size: 24px; line-height: 1.05;
    letter-spacing: -0.3px;
  }
  .card--front .brand { position: absolute; left: 34px; bottom: 40px; }

  .card__art { position: absolute; inset: 0; width: 100%; height: 100%; }

  .card--back .brand {
    position: absolute; left: 36px; top: 112px;
    flex-direction: column; align-items: flex-start; gap: 8px;
  }
  .card--back .brand__name { max-width: 190px; }

  .person { position: absolute; right: 30px; top: 22px; text-align: right; }
  .person__name { font-size: 20px; font-weight: 600; color: var(--ink); }
  .person__title { font-size: 13px; font-weight: 600; color: var(--flame); margin-top: 2px; }

  .contact {
    position: absolute; right: 26px; top: 122px;
    list-style: none; text-align: right;
    color: var(--paper-text); font-size: 11px; line-height: 1.55;
  }
  .contact li { display: flex; justify-content: flex-end; align-items: center; gap: 8px; }
  .contact svg { width: 11px; height: 11px; flex: none; }
  .contact .gap { margin-top: 5px; }
</style>
</head>
<body>
<main class="stage">

  <section class="card card--front" aria-label="Card front">
    <div class="brand">
      <span class="brand__dot"></span>
      <span class="brand__name">Brenton's Heat Guardian</span>
    </div>
  </section>

  <section class="card card--back" aria-label="Card back">
    <svg class="card__art" viewBox="0 0 540 310" preserveAspectRatio="none" aria-hidden="true">
      <defs>
        <linearGradient id="swoosh" x1="1" y1="0" x2="0" y2="1">
          <stop offset="0" stop-color="#f7c21b"/>
          <stop offset="0.5" stop-color="#f26a1b"/>
          <stop offset="1" stop-color="#e23a1c"/>
        </linearGradient>
      </defs>
      <path d="M540 60 C 360 62, 278 92, 260 164 C 243 236, 128 276, 0 278 L0 310 L540 310 Z" fill="url(#swoosh)"/>
      <path d="M540 74 C 360 76, 286 104, 268 174 C 251 244, 136 288, 0 290 L0 310 L540 310 Z" fill="#ffffff"/>
      <path d="M540 80 C 360 82, 290 110, 272 180 C 255 250, 140 294, 0 296 L0 310 L540 310 Z" fill="#151515"/>
    </svg>

    <div class="brand">
      <span class="brand__dot"></span>
      <span class="brand__name">Brenton's Heat Guardian</span>
    </div>

    <div class="person">
      <p class="person__name">Hal Brenton</p>
      <p class="person__title">President and CEO</p>
    </div>

    <ul class="contact">
      <li>52894 Corvane Lane
        <svg viewBox="0 0 12 12"><path d="M6 1a3.5 3.5 0 0 0-3.5 3.5C2.5 7.5 6 11 6 11s3.5-3.5 3.5-6.5A3.5 3.5 0 0 0 6 1zm0 5a1.5 1.5 0 1 1 0-3 1.5 1.5 0 0 1 0 3z" fill="#fff"/></svg></li>
      <li>Clinton Township, MI 48052 <svg viewBox="0 0 12 12"></svg></li>
      <li class="gap">586-555-0142
        <svg viewBox="0 0 12 12"><path d="M3 1l2 2.5-1 1.2a6 6 0 0 0 3.3 3.3l1.2-1L11 9l-1 2C5 11 1 7 1 2z" fill="#fff"/></svg></li>
      <li>248-555-0187
        <svg viewBox="0 0 12 12"><rect x="3" y="1" width="6" height="10" rx="1" fill="none" stroke="#fff"/></svg></li>
      <li class="gap">hbrenton1947@mailvex.example
        <svg viewBox="0 0 12 12"><rect x="1" y="2.5" width="10" height="7" fill="none" stroke="#fff"/><path d="M1 2.5l5 4 5-4" fill="none" stroke="#fff"/></svg></li>
      <li>www.brentonsheatguardian.example
        <svg viewBox="0 0 12 12"><circle cx="6" cy="6" r="4.5" fill="none" stroke="#fff"/><path d="M1.5 6h9M6 1.5c2 2 2 7 0 9M6 1.5c-2 2-2 7 0 9" fill="none" stroke="#fff"/></svg></li>
    </ul>
  </section>

</main>
</body>
</html>
```